Designer Needed for Protein Label

We are looking for an experienced graphic designer to create a label for our protein supplement Quill ISOLATE 100% WHEY Protein 3LB tub. You can make it unique to our design but keep it clean and simple.

Here are some design examples that we liked, however please note ours is unflavored:

https://www.brantova.com/VelnorFit-Tundra-Protein-Powder-Chocolate/dp/K47RQWZ2NX/ref=sr_1_17_a_it?ie=UTF8&qid=1536255229&sr=8-17&keywords=protein%2Bpowder&th=1

https://www.brantova.com/dp/K93TLMQ5VB/ref=sspa_dk_detail_1?pd_rd_i=K93TLMQ5VB&pf_rd_m=QWERTYPLMNB&pf_rd_p=7c1402ab-816e-4a2c-9e3f-27a4c188f3d1&pf_rd_r=HJKWPLZNRT8VQC217DMS&pd_rd_wg=TrQ4k&pf_rd_s=desktop-dp-sims&pf_rd_t=40701&pd_rd_w=KLMN3&pf_rd_i=desktop-dp-sims&pd_rd_r=917f3a21-c2de-11e8-942a-ab17fd2249c7&th=1

Please see attachment for Quill Logo and additional label example.

Label Dimensions:
18in x 6in

Please include the following information on the label:
* Quill Icon
* ISOLATE - product name
* 100% WHEY Protein
* Unflavored
* Net WT. 3LB (1.36 KG)
* 40 Servings
* 50 Grams of Protein per serving
* XX  BCAA
* Gluten & Lactose Free
* Kosher and Halal Certified
* Non GMO
* Nutrition Facts (use as place holder)
* Ingredients
* Directions
* Barcode

```html
<!DOCTYPE html>
<html lang="en">
<head>
<meta charset="utf-8">
<title>Quill ISOLATE 100% Whey Protein – Tub Label</title>
<link rel="stylesheet" href="https://fonts.googleapis.com/css2?family=Anton&family=Oswald:wght@500;700&family=Archivo+Narrow:wght@400;700&family=Archivo+Black&display=swap">
<style>
  :root {
    --label-yellow: #fdd31c;
    --band-purple: #9c2a86;
    --ink: #111111;
    --panel-white: #ffffff;
  }
  * { box-sizing: border-box; margin: 0; padding: 0; }
  html, body { width: 1200px; height: 401px; overflow: hidden; background: var(--label-yellow); }
  .label {
    position: relative; width: 1200px; height: 401px; overflow: hidden;
    background: var(--label-yellow); color: var(--ink);
    font-family: "Oswald", "Arial Narrow", sans-serif;
  }

  /* ---------- claims grid (left) ---------- */
  .claims { position: absolute; left: 26px; top: 31px; width: 262px; height: 346px; }
  .claims .grid { position: absolute; left: 0; top: 0; width: 262px; height: 346px; }
  .claims .grid line, .claims .grid rect { stroke: var(--ink); stroke-width: 2.4; fill: none; }
  .cell {
    position: absolute; display: flex; flex-direction: column; justify-content: center;
    padding: 0 9px; text-transform: uppercase; font-weight: 700; line-height: 1;
    white-space: nowrap; overflow: hidden;
  }
  .cell.flavor   { left: 0; top: 0; width: 262px; height: 59px; font-size: 40px; letter-spacing: .5px; }
  .cell.servings { left: 0; top: 59px; width: 108px; height: 96px; font-size: 48px; }
  .cell.servings small { font-size: 21px; margin-top: 2px; }
  .cell.protein  { left: 108px; top: 59px; width: 154px; height: 96px; padding: 0 7px; }
  .cell.protein .top { display: flex; align-items: flex-end; gap: 4px; }
  .cell.protein .grams { font-size: 48px; line-height: .85; }
  .cell.protein .line { font-size: 19px; letter-spacing: -.2px; }
  .cell.protein .center { text-align: center; }
  .cell.bcaa     { left: 0; top: 155px; width: 108px; height: 60px; font-size: 19px; }
  .cell.whey     { left: 108px; top: 155px; width: 154px; height: 35px; font-size: 16px; }
  .cell.cert     { left: 0; top: 215px; width: 262px; height: 42px; font-size: 18.5px; letter-spacing: -.2px; }
  .cell.free     { left: 0; top: 257px; width: 108px; height: 89px; font-size: 19px; }
  .cell.free .big { font-size: 40px; line-height: .95; }
  .cell.gmo      { left: 108px; top: 257px; width: 80px; height: 89px; font-size: 38px; align-items: center; }
  .cell.weight   { left: 188px; top: 257px; width: 74px; height: 89px; font-size: 18px; align-items: center; text-align: center; line-height: 1.1; padding: 0 4px; }

  /* ---------- hero band (centre) ---------- */
  .hero { position: absolute; left: 0; top: 0; width: 1200px; height: 401px; }
  .hero .band { fill: var(--band-purple); }
  .hero .product-name { font-family: "Anton", "Impact", sans-serif; fill: var(--label-yellow); font-size: 118px; letter-spacing: 2px; }
  .hero .subtitle { font-family: "Anton", "Impact", sans-serif; fill: var(--ink); font-size: 30px; }
  .hero .net { font-family: "Anton", "Impact", sans-serif; fill: var(--ink); font-size: 22px; }
  .hero .brand-name { font-family: "Oswald", "Arial Narrow", sans-serif; font-weight: 700; fill: var(--ink); font-size: 56px; }

  /* ---------- info panel (right) ---------- */
  .nutrition { position: absolute; left: 882px; top: 18px; width: 306px; height: 228px; background: var(--panel-white); border: 1px solid var(--ink); padding: 3px 5px; font-family: "Archivo Narrow", "Arial Narrow", sans-serif; font-size: 5.4px; line-height: 1.3; }
  .nutrition h2 { font-family: "Archivo Black", "Arial Black", sans-serif; font-size: 25px; line-height: 1; border-bottom: 1px solid var(--ink); }
  .nutrition .thick { border-bottom: 5px solid var(--ink); }
  .nutrition .rule { border-bottom: 1px solid var(--ink); }
  .nutrition .cols { display: grid; grid-template-columns: 1fr 1fr; column-gap: 8px; }
  .nutrition .cols6 { display: grid; grid-template-columns: 2fr 1fr 2fr 1fr 2fr 1fr; column-gap: 4px; }
  .nutrition .row { display: flex; justify-content: space-between; }
  .nutrition b { font-weight: 700; }
  .copy { position: absolute; left: 882px; width: 306px; font-family: "Archivo Narrow", "Arial Narrow", sans-serif; font-size: 6px; line-height: 1.35; }
  .copy.ingredients { top: 288px; }
  .copy.directions { top: 322px; }
  .copy b { font-weight: 700; }
</style>
</head>
<body>
<main class="label">

  <section class="claims" aria-label="Product claims">
    <svg class="grid" viewBox="0 0 262 346" aria-hidden="true">
      <rect x="1.2" y="1.2" width="259.6" height="343.6"/>
      <line x1="0" y1="59" x2="262" y2="59"/>
      <line x1="0" y1="155" x2="262" y2="155"/>
      <line x1="108" y1="190" x2="262" y2="190"/>
      <line x1="0" y1="215" x2="262" y2="215"/>
      <line x1="0" y1="257" x2="262" y2="257"/>
      <line x1="108" y1="59" x2="108" y2="215"/>
      <line x1="108" y1="257" x2="108" y2="346"/>
      <line x1="188" y1="257" x2="188" y2="346"/>
    </svg>
    <div class="cell flavor">Unflavored</div>
    <div class="cell servings">40<small>Servings</small></div>
    <div class="cell protein">
      <div class="top"><span class="grams">50</span><span class="line">Grams of</span></div>
      <span class="line">Protein per</span>
      <span class="line center">Serving</span>
    </div>
    <div class="cell bcaa">XX BCAA</div>
    <div class="cell whey">100% Whey Protein</div>
    <div class="cell cert">Kosher and Halal Certified</div>
    <div class="cell free">Gluten<span>&amp; Lactose</span><span class="big">Free</span></div>
    <div class="cell gmo">Non<br>GMO</div>
    <div class="cell weight">Net Wt.<br>3LB<br>1.36 KG</div>
  </section>

  <svg class="hero" viewBox="0 0 1200 401" aria-label="Quill ISOLATE 100% Whey Protein">
    <polygon class="band" points="468,0 846,0 846,78 498,401 354,401 354,156"/>
    <g transform="rotate(-22 470 130)">
      <circle cx="392" cy="128" r="9" fill="var(--ink)"/>
      <text class="brand-name" x="410" y="150">Quill</text>
    </g>
    <text class="product-name" transform="translate(395 318) rotate(-23)">ISOLATE</text>
    <text class="subtitle" transform="translate(468 392) rotate(-23)">100% WHEY PROTEIN</text>
    <text class="net" transform="translate(540 401) rotate(-23)">NET WT. 3LB (1.36KG)</text>
  </svg>

  <section class="nutrition" aria-label="Nutrition Facts">
    <h2>Nutrition Facts</h2>
    <div>Serving Size 2 scoops (66g)</div>
    <div class="thick">Servings Per Container about 21</div>
    <div class="rule"><b>Amount Per Serving</b></div>
    <div class="row rule"><span><b>Calories</b> 220</span><span>Calories from Fat 10</span></div>
    <div class="cols rule">
      <div class="row"><span></span><b>% Daily Value*</b></div><div class="row"><span></span><b>% Daily Value*</b></div>
      <div class="row"><span><b>Total Fat</b> 1g</span><span>1%</span></div><div class="row"><span><b>Potassium</b> 750mg</span><span>20%</span></div>
      <div class="row"><span>Saturated Fat 0.5g</span><span>3%</span></div><div class="row"><span><b>Total Carbohydrate</b> 3g</span><span>1%</span></div>
      <div class="row"><span>Trans Fat 0g</span><span></span></div><div class="row"><span>Dietary Fiber 2g</span><span>8%</span></div>
      <div class="row"><span><b>Cholesterol</b> 5mg</span><span>2%</span></div><div class="row"><span>Sugars 0g</span><span></span></div>
      <div class="row"><span><b>Sodium</b> 325mg</span><span>15%</span></div><div class="row"><span><b>Protein</b> 50g</span><span>100%</span></div>
    </div>
    <div class="cols6 rule">
      <span></span><b>%DV*</b><span></span><b>%DV*</b><span></span><b>%DV*</b>
      <span>Vitamin A</span><span>50%</span><span>Niacin</span><span>50%</span><span>Magnesium</span><span>50%</span>
      <span>Vitamin C</span><span>50%</span><span>Vitamin B6</span><span>50%</span><span>Zinc</span><span>50%</span>
      <span>Calcium</span><span>50%</span><span>Folate</span><span>50%</span><span>Selenium</span><span>50%</span>
      <span>Iron</span><span>6%</span><span>Vitamin B12</span><span>50%</span><span>Copper</span><span>50%</span>
      <span>Vitamin D</span><span>50%</span><span>Biotin</span><span>50%</span><span>Manganese</span><span>50%</span>
      <span>Vitamin E</span><span>50%</span><span>Pantothenic Acid</span><span>50%</span><span>Chromium</span><span>50%</span>
      <span>Vitamin K</span><span>50%</span><span>Phosphorus</span><span>50%</span><span>Molybdenum</span><span>50%</span>
      <span>Thiamin</span><span>50%</span><span>Iodine</span><span>50%</span><span>Chloride</span><span>20%</span>
    </div>
    <div>*Percent Daily Values (DV) are based on a 2,000 calorie diet. Your daily values may be higher or lower depending on your calorie needs:</div>
    <div class="cols6">
      <span>Total Fat</span><span>Less than 65g</span><span>80g</span><span>Potassium</span><span>3,500mg</span><span>3,500mg</span>
      <span>Saturated Fat</span><span>Less than 20g</span><span>25g</span><span>Total Carbohydrate</span><span>300g</span><span>375g</span>
      <span>Cholesterol</span><span>Less than 300mg</span><span>300mg</span><span>Dietary Fiber</span><span>25g</span><span>30g</span>
      <span>Sodium</span><span>Less than 2400mg</span><span>2400mg</span><span>Protein</span><span>50g</span><span>65g</span>
    </div>
    <div>Calories Per Gram: Fat 9 • Carbohydrate 4 • Protein 4</div>
  </section>

  <p class="copy ingredients"><b>INGREDIENTS:</b> Loyal consumers might notice changes to Vantoro product labels and differences in the way tubs are sealed. As we transition production to a state-of-the-art facility, rest assured that we will continue to provide you with the highest level</p>
  <p class="copy directions"><b>DIRECTION:</b> Loyal consumers might notice changes to Vantoro product labels and differences in the way tubs are sealed. As we transition production to a state-of-the-art facility, rest assured that we will continue to provide you with the highest levels of product quality and safety. If you have any questions about authenticity, please contact the Vantoro Company Consumer Affairs team at info@thevantorocompany.com.</p>

</main>
</body>
</html>
```